Brenford Journeys Corporation – 2026 Corporate Events Calendar (Update from 2025)

We require an updated 2026 Events Calendar for Brenford Journeys Corporation, replacing the existing 2025 version.
This calendar is produced annually and shared with corporate clients as a practical planning tool highlighting key dates that impact business travel.

The design should feel premium, corporate, and polished, consistent with Brenford Journeys’s brand.

Content to Include (2026)

The calendar must clearly present:
1. 2026 School Terms (Australia-wide)
• NSW (Eastern & Western), ACT, VIC, QLD, NT, WA, SA, TAS
2. 2026 Australian Public Holidays
• National and state-based
• Clearly labelled by state
3. 2026 Key Australian Events
• Major sporting events
• Cultural festivals
• Business-impacting events (e.g. Grand Finals, major festivals)

Content will be supplied
— the designer’s role is layout, hierarchy, and presentation.

⸻
Branding & Style
• Brand: Brenford Journeys Corporation
• Tone: Corporate, confident, premium, understated
• Audience: Corporate travel managers, executives, EAs
• Look & Feel:
• Modern
• Professional
• Not cluttered
• Clear visual hierarchy
• Avoid anything playful, loud, or consumer-travel focused

⸻

Logos & References
• Use existing Brenford Journeys Corporation branding
• Wayplume logo may appear if it exists in the current calendar
• Designer should follow the current 2025 calendar layout as reference

⸻

Deliverables
• Final PDF (print-ready)
• Editable source file (InDesign or Illustrator preferred)

⸻

Inspiration / Reference
• Current 2025 Brenford Journeys Events Calendar (supplied)
→ The 2026 version should feel like a natural evolution, not a redesign.

⸻

Key Success Criteria
• Instantly usable by corporate clients
• Clear dates at a glance
• Feels authoritative and trustworthy
• Looks like it belongs in a boardroom, not a brochure rack

```html
<!DOCTYPE html>
<html lang="en">
<head>
<meta charset="utf-8">
<title>Brenford Journeys Corporation – 2026 Events Calendar</title>
<link rel="stylesheet" href="https://fonts.googleapis.com/css2?family=Poppins:wght@500;600&family=Inter:wght@600&display=swap">
<style>
  :root {
    --backdrop: #e9ecef;
    --navy: #03173a;
    --brand-navy: #1f3f7f;
    --brand-grey: #8c8c8c;
    --accent-blue: #1d9ce6;
    --white: #ffffff;
    --faint: #e8d9c8;
  }
  * { margin: 0; padding: 0; box-sizing: border-box; }
  html, body {
    width: 1200px; height: 1200px; overflow: hidden;
    background: var(--backdrop);
  }
  .cover {
    position: absolute; left: 197px; top: 30px;
    width: 806px; height: 1140px;
    background: var(--white);
    overflow: hidden;
  }
  .cover__panel {
    position: absolute; left: 0; top: 0;
    width: 408px; height: 100%;
    background: var(--navy);
  }
  .cover__photo {
    position: absolute; left: 408px; width: 398px;
  }
  .cover__photo--upper {
    top: 0; height: 551px;
    background: linear-gradient(160deg, #f4f4f2 0%, #e6e4df 45%, #3d5a4d 75%, #5a4436 100%);
  }
  .cover__photo--lower {
    top: 648px; height: 492px;
    background: linear-gradient(170deg, #3c5c4c 0%, #d9b98f 35%, #e7cfa9 65%, #cfae85 100%);
  }
  .brand-band {
    position: absolute; left: 408px; top: 551px;
    width: 398px; height: 97px;
    background: var(--white);
    display: flex; align-items: center; justify-content: space-between;
    padding: 0 28px 0 36px;
  }
  .brand-band__name {
    font-family: "Poppins", sans-serif; font-weight: 600;
    line-height: 1.05;
  }
  .brand-band__name--primary { color: var(--brand-navy); font-size: 18px; }
  .brand-band__name--partner { color: var(--brand-grey); font-size: 27px; }
  .cover__title {
    position: absolute; left: 35px; top: 828px;
    font-family: "Poppins", sans-serif; font-weight: 500;
    font-size: 70px; line-height: 69px; letter-spacing: -0.5px;
    color: var(--white);
  }
  .contact-line {
    position: absolute; left: 35px; top: 1092px;
    display: flex; align-items: center;
    font-family: "Inter", sans-serif; font-weight: 600;
    font-size: 12.5px; color: var(--white);
  }
  .contact-line__label { width: 238px; }
  .contact-line__chip {
    background: var(--accent-blue);
    height: 26px; line-height: 26px;
    padding: 0 11px;
  }
  .contact-line__chip--email { width: 220px; }
  .contact-line__chip--web { width: 210px; }
  .contact-line__sep {
    width: 63px; text-align: center;
    color: var(--faint); opacity: 0.5;
  }
</style>
</head>
<body>
  <main class="cover">
    <div class="cover__panel"></div>
    <div class="cover__photo cover__photo--upper" role="img" aria-label="Photo of two colleagues smiling as they plan together at a desk"></div>
    <div class="brand-band">
      <div class="brand-band__name brand-band__name--primary">Brenford Journeys<br>Corporation</div>
      <div class="brand-band__name brand-band__name--partner">Wayplume</div>
    </div>
    <div class="cover__photo cover__photo--lower" role="img" aria-label="Photo of a wooden desk with notebooks, sticky notes, phones and hands writing"></div>
    <h1 class="cover__title">2026<br>Events<br>Calendar</h1>
    <p class="contact-line">
      <span class="contact-line__label">For more information contact us at</span>
      <span class="contact-line__chip contact-line__chip--email">sales@brenfordjourneys.com.au</span>
      <span class="contact-line__sep">or visit</span>
      <span class="contact-line__chip contact-line__chip--web">www.brenfordjourneys.com.au</span>
    </p>
  </main>
</body>
</html>
```